Software company WebSite Design (enterprise level SW, Mobile apps, HW prototypes)

We need design for our new webpages. We got new logo and new business cards and we need webdesign which will be match with those two.
We are dealing with corporate level software development - enterprise level portals, development of optimalization SW, route planning optimalizations. For a few months we are developing mobile applications for companies.
IMPORTANT is to express the cutting edge technological company.

Target Market(s)

IT company customers

Industry/Entity Type

Business

Number of Pages Required

2 page

Requirements
Must have
• Project needs to have landing page and product detail page. Design needs to be created including full font and example images as there would be a real webpage. Design should be clean, modern and expressing hi-tech level of the company.
• Example of well designer web pages - www.quorvelt.com, www.brandissa.com - We like the font formatting and font designs (colors, placing, etc - its professional).
• Attached image contains screenshot from old web landing page. It contains basic sections of our business (Simulation Tools, Enterprise Intranet Systems, Hi-tech web presentations, Supporting Enterprise services - Optimalization and logistics monitoring)

```html
<!DOCTYPE html>
<html lang="en">
<head>
<meta charset="utf-8">
<title>Kelvaro Solutions</title>
<link href="https://fonts.googleapis.com/css2?family=Open+Sans:wght@400;600;700;800&display=swap" rel="stylesheet">
<style>
:root{
  --orange:#e8612c;
  --blue:#1aa3dc;
  --navy:#0d2f52;
  --dark:#2b2e33;
  --darker:#202226;
  --grey:#8a8f96;
  --light:#f3f4f6;
  --page:#e9ebee;
  --white:#ffffff;
}
*{margin:0;padding:0;box-sizing:border-box}
html,body{width:724px;height:1200px;overflow:hidden}
body{background:var(--page);font-family:"Open Sans",Arial,sans-serif;color:var(--dark)}
.site{position:absolute;left:43px;top:10px;width:638px;height:1180px;background:var(--white);box-shadow:0 2px 10px rgba(0,0,0,.18);overflow:hidden}

/* hero */
.hero{position:absolute;left:0;top:0;width:638px;height:300px;
  background:radial-gradient(ellipse at 30% 40%,#7fd0f2 0%,#2a8fcf 30%,#15568f 65%,#0b2f55 100%)}
.header{position:absolute;left:0;top:0;width:638px;height:40px;display:flex;align-items:center;justify-content:space-between;padding:0 18px;background:rgba(8,30,55,.35)}
.brand{display:flex;align-items:center;gap:7px;color:var(--white);font-weight:800;font-size:17px;letter-spacing:1px}
.brand-mark{width:18px;height:18px;background:var(--orange)}
.nav{display:flex;gap:4px;font-size:8px;font-weight:600;color:var(--white)}
.nav a{color:inherit;text-decoration:none;padding:6px 8px}
.nav a.active{background:var(--blue)}

/* services */
.services{position:absolute;left:0;top:294px;width:638px;display:flex}
.service{width:127.6px;display:flex;flex-direction:column;align-items:center}
.ring{width:92px;height:92px;border-radius:50%;background:var(--white);border:6px solid var(--orange);display:flex;align-items:center;justify-content:center;box-shadow:0 2px 4px rgba(0,0,0,.2)}
.ring-inner{width:70px;height:70px;border-radius:50%;border:2px solid #d7dadf;display:flex;align-items:center;justify-content:center}
.service-name{margin-top:10px;font-size:8.5px;font-weight:700;text-align:center;line-height:1.3;color:var(--dark)}

/* about */
.about{position:absolute;left:0;top:462px;width:638px;height:160px;background:linear-gradient(180deg,#23262c,#1b2d44 60%,#153a63);color:var(--white);text-align:center;padding-top:16px}
.section-title{display:flex;align-items:center;justify-content:center;gap:12px;font-size:15px;font-weight:700;letter-spacing:.5px}
.section-title::before,.section-title::after{content:"";width:150px;height:1px;background:rgba(255,255,255,.5)}
.dot{width:9px;height:9px;background:var(--orange);transform:rotate(45deg);margin:8px auto 8px}
.about p{width:560px;margin:0 auto;font-size:8px;line-height:1.55;color:#d9dee5}
.btn{display:inline-block;margin-top:10px;padding:5px 16px;background:var(--blue);color:var(--white);font-size:7.5px;font-weight:700}

/* blog & contact */
.content{position:absolute;left:0;top:646px;width:638px;height:290px;display:flex;padding:0 34px;gap:36px}
.blog{width:320px}
.contact{width:214px}
.block-title{font-size:15px;font-weight:600;text-align:center;color:var(--dark)}
.block-dot{width:8px;height:8px;background:var(--orange);transform:rotate(45deg);margin:8px auto 14px}
.post{display:flex;gap:12px;margin-bottom:14px}
.date{width:42px;text-align:center;flex-shrink:0}
.date .day{background:var(--orange);color:var(--white);font-size:17px;font-weight:700;line-height:22px}
.date .mon{background:var(--orange);color:var(--white);font-size:7px;font-weight:700;border-top:1px solid rgba(255,255,255,.5)}
.date .yr{font-size:7px;color:var(--grey);margin-top:2px}
.post h3{font-size:8.5px;font-weight:700;margin-bottom:3px}
.post p{font-size:7.5px;line-height:1.45;color:#555b62}
.form .field{height:20px;border:1px solid #d2d5d9;background:var(--light);font-size:7px;color:var(--grey);padding:5px 8px;margin-bottom:7px}
.form .msg{height:50px}
.send{display:inline-block;padding:5px 14px;background:var(--dark);color:var(--white);font-size:7px;font-weight:700}

/* footer */
.footer{position:absolute;left:0;top:952px;width:638px;height:198px;background:var(--dark);display:flex;padding:22px 34px 0;gap:28px;color:#c9ccd1}
.col h4{font-size:8.5px;font-weight:700;color:var(--orange);margin-bottom:8px}
.col li{list-style:none;font-size:7.5px;line-height:1.6;color:var(--white)}
.col.links{width:90px}
.col.serv{width:150px}
.col.info{width:140px}
.info li{display:flex;align-items:flex-start;gap:6px;margin-bottom:5px}
.ico{width:11px;height:11px;flex-shrink:0;margin-top:1px}
.footer-brand{margin-left:auto;display:flex;flex-direction:column;align-items:center;padding-top:6px}
.footer-brand .brand{font-size:20px}
.footer-brand .brand-mark{width:24px;height:24px}
.social{display:flex;gap:5px;margin-top:16px}
.social span{width:16px;height:16px;border-radius:50%;background:#5a5e65}
.copyright{position:absolute;left:0;top:1150px;width:638px;height:30px;background:var(--darker);color:#9a9ea5;font-size:6.5px;text-align:center;line-height:30px}
</style>
</head>
<body>
<div class="site">

  <section class="hero" role="img" aria-label="Businessman touching a glowing holographic technology interface on a blue background"></section>

  <header class="header">
    <div class="brand"><span class="brand-mark"></span>KELVARO</div>
    <nav class="nav">
      <a class="active" href="#">HOME</a><a href="#">ABOUT US</a><a href="#">SERVICES ▾</a><a href="#">BLOG</a><a href="#">CONTACT</a>
    </nav>
  </header>

  <section class="services">
    <div class="service">
      <div class="ring"><div class="ring-inner">
        <svg width="32" height="32" viewBox="0 0 32 32" fill="none" stroke="#1aa3dc" stroke-width="2"><path d="M16 5 28 11 16 17 4 11Z"/><path d="M4 16l12 6 12-6"/><path d="M4 21l12 6 12-6"/></svg>
      </div></div>
      <div class="service-name">SOFTWARE<br>DEVELOPMENT</div>
    </div>
    <div class="service">
      <div class="ring"><div class="ring-inner">
        <svg width="32" height="32" viewBox="0 0 32 32" fill="none" stroke="#1aa3dc" stroke-width="2"><rect x="4" y="6" width="24" height="20"/><path d="M4 11h24M10 16h12M10 20h8"/></svg>
      </div></div>
      <div class="service-name">ENTERPRISE LEVEL<br>PORTALS</div>
    </div>
    <div class="service">
      <div class="ring"><div class="ring-inner">
        <svg width="32" height="32" viewBox="0 0 32 32" fill="none" stroke="#1aa3dc" stroke-width="2"><rect x="4" y="5" width="24" height="17"/><path d="M12 27h8M16 22v5"/><circle cx="16" cy="13.5" r="4"/></svg>
      </div></div>
      <div class="service-name">SOFTWARE<br>OPTIMIZATION</div>
    </div>
    <div class="service">
      <div class="ring"><div class="ring-inner">
        <svg width="32" height="32" viewBox="0 0 32 32" fill="none" stroke="#1aa3dc" stroke-width="2"><circle cx="8" cy="24" r="3"/><circle cx="24" cy="8" r="3"/><path d="M11 24h9a4 4 0 0 0 0-8h-8a4 4 0 0 1 0-8h9"/></svg>
      </div></div>
      <div class="service-name">ROUTE PLANNING<br>OPTIMIZATION</div>
    </div>
    <div class="service">
      <div class="ring"><div class="ring-inner">
        <svg width="32" height="32" viewBox="0 0 32 32" fill="none" stroke="#1aa3dc" stroke-width="2"><rect x="6" y="4" width="14" height="24" rx="2"/><rect x="17" y="11" width="10" height="15" rx="1.5"/><path d="M12 24h2"/></svg>
      </div></div>
      <div class="service-name">MOBILE APPLICATIONS</div>
    </div>
  </section>

  <section class="about">
    <h2 class="section-title">ABOUT KELVARO SOLUTIONS</h2>
    <div class="dot"></div>
    <p>We build enterprise software that scales with your business. From intranet portals and optimization engines to route planning and mobile apps, our team turns complex processes into clear, reliable tools. Every project starts with listening, continues with careful engineering and ends with support that keeps your systems running day after day.</p>
    <span class="btn">LEARN MORE</span>
  </section>

  <section class="content">
    <div class="blog">
      <h2 class="block-title">LATEST FROM THE BLOG</h2>
      <div class="block-dot"></div>
      <article class="post">
        <div class="date"><div class="day">01</div><div class="mon">MAY</div><div class="yr">2014</div></div>
        <div><h3>Blog #1</h3><p>Notes from our team on portals, optimization and mobile work for enterprise clients.</p></div>
      </article>
      <article class="post">
        <div class="date"><div class="day">24</div><div class="mon">APR</div><div class="yr">2014</div></div>
        <div><h3>Blog #2</h3><p>How smarter route planning cuts fleet costs and keeps deliveries on schedule.</p></div>
      </article>
      <article class="post">
        <div class="date"><div class="day">15</div><div class="mon">APR</div><div class="yr">2014</div></div>
        <div><h3>Blog #3</h3><p>A short look at building secure mobile apps for large internal teams.</p></div>
      </article>
    </div>
    <div class="contact">
      <h2 class="block-title">CONTACT</h2>
      <div class="block-dot"></div>
      <div class="form">
        <div class="field">Name</div>
        <div class="field">Email</div>
        <div class="field">Phone</div>
        <div class="field msg">Message</div>
        <span class="send">SEND</span>
      </div>
    </div>
  </section>

  <footer class="footer">
    <div class="col links">
      <h4>QUICK LINKS</h4>
      <ul><li>HOME</li><li>ABOUT US</li><li>BLOG</li><li>CONTACT</li></ul>
    </div>
    <div class="col serv">
      <h4>SERVICES</h4>
      <ul><li>SOFTWARE DEVELOPMENT</li><li>ENTERPRISE LEVEL PORTAL</li><li>SOFTWARE OPTIMIZATION</li><li>ROUTE PLANNING</li><li>MOBILE APPLICATIONS</li></ul>
    </div>
    <div class="col info">
      <h4>CONTACT</h4>
      <ul>
        <li><svg class="ico" viewBox="0 0 12 12" fill="#e8612c"><path d="M6 0a4 4 0 0 0-4 4c0 3 4 8 4 8s4-5 4-8a4 4 0 0 0-4-4Zm0 5.5A1.5 1.5 0 1 1 6 2.5a1.5 1.5 0 0 1 0 3Z"/></svg><span>Lindral 412<br>20518 Varnholt</span></li>
        <li><svg class="ico" viewBox="0 0 12 12" fill="#e8612c"><path d="M2.5 0 4.5 2.5 3.3 4a7 7 0 0 0 4.7 4.7L9.5 7.5 12 9.5 10.5 12C5 12 0 7 0 1.5Z"/></svg><span>+00 555 018 224</span></li>
        <li><svg class="ico" viewBox="0 0 12 12" fill="none" stroke="#e8612c" stroke-width="1.3"><rect x="0.7" y="2" width="10.6" height="8"/><path d="M1 2.5 6 6.5 11 2.5"/></svg><span>hello@kelvaro.io</span></li>
      </ul>
    </div>
    <div class="footer-brand">
      <div class="brand"><span class="brand-mark"></span>KELVARO</div>
      <div class="social"><span></span><span></span><span></span><span></span><span></span></div>
    </div>
  </footer>
  <div class="copyright">© 2014 KELVARO SOLUTIONS. ALL RIGHTS RESERVED.</div>

</div>
</body>
</html>
```